stationary for hygienic company

We need a stationary design for hygienic company which provides public high end sanitary products and high end public lavatory.
We need a fresh and clean style stationary
we want the following things:
* logo (redesigned in eps/vector)
* Letterhead (with company details)
* letterhead (without company details)
* Business card
* note block
* ballpoint
* etcetera (a complete package)

```html
<!DOCTYPE html>
<html lang="fr">
<head>
<meta charset="utf-8">
<title>Mirelle – Letterhead</title>
<link rel="stylesheet" href="https://fonts.googleapis.com/css2?family=Quicksand:wght@400;500&display=swap">
<style>
  :root {
    --paper: #ffffff;
    --ink: #2b2b2e;
    --ink-soft: #6d6d72;
    --accent-blue: #1b9ad8;
    --accent-navy: #1f2170;
    --accent-pink: #ec3f8c;
    --rail-grey: #bdb9b9;
  }
  html, body {
    margin: 0;
    padding: 0;
    overflow: hidden;
    background: var(--paper);
  }
  .letterhead {
    position: relative;
    width: 849px;
    height: 1200px;
    background: var(--paper);
    overflow: hidden;
    font-family: "Quicksand", sans-serif;
    color: var(--ink);
  }
  .brand {
    position: absolute;
    left: 96px;
    top: 92px;
    display: flex;
    align-items: center;
    gap: 48px;
  }
  .brand__text {
    display: flex;
    flex-direction: column;
    align-items: center;
  }
  .brand__name {
    font-size: 46px;
    font-weight: 400;
    letter-spacing: 0.5px;
    line-height: 1;
    color: var(--ink);
  }
  .brand__tagline {
    margin-top: 8px;
    font-size: 14px;
    line-height: 1;
    color: var(--ink);
  }
  .brand__place {
    margin-top: 6px;
    font-size: 7px;
    line-height: 1;
    color: var(--ink-soft);
  }
  .brand__dot {
    width: 58px;
    height: 58px;
    border-radius: 50%;
    background: var(--accent-pink);
  }
  .side-rail {
    position: absolute;
    top: 0;
    right: 0;
    width: 20px;
    height: 1200px;
  }
</style>
</head>
<body>
  <main class="letterhead">
    <header class="brand">
      <div class="brand__text">
        <span class="brand__name">Mirelle</span>
        <span class="brand__tagline">Boutique Hygienique</span>
        <span class="brand__place">Paris · Genève</span>
      </div>
      <span class="brand__dot" aria-hidden="true"></span>
    </header>

    <svg class="side-rail" viewBox="0 0 20 1200" aria-hidden="true">
      <defs>
        <linearGradient id="rail-fade" x1="0" y1="0" x2="0" y2="1">
          <stop offset="0" stop-color="var(--rail-grey)" stop-opacity="0"/>
          <stop offset="1" stop-color="var(--rail-grey)" stop-opacity="1"/>
        </linearGradient>
      </defs>
      <rect x="0" y="330" width="20" height="434" fill="url(#rail-fade)"/>
      <rect x="0" y="764" width="20" height="193" fill="var(--accent-blue)"/>
      <rect x="0" y="957" width="20" height="33" fill="var(--accent-navy)"/>
      <rect x="0" y="990" width="20" height="63" fill="var(--accent-pink)"/>
      <rect x="0" y="1053" width="20" height="147" fill="var(--rail-grey)"/>
    </svg>
  </main>
</body>
</html>
```